Investment Business - Biz Card Design

Using the attached logo files, please create a superior business card design for Tarnwell Holdings.

The "back" of the card should feature the logo (either in colour, or white/black over a feature colour)

The "front" of the card should feature: name, email, and phone

The design should be minimal and clean.

Target Market(s)

Business owners who need our investment services.

Industry/Entity Type

Business

```html
<!DOCTYPE html>
<html lang="en">
<head>
<meta charset="utf-8">
<title>Tarnwell Holdings – Business Card</title>
<link href="https://fonts.googleapis.com/css2?family=Open+Sans:wght@400;600;700&display=swap" rel="stylesheet">
<style>
  :root {
    --bg: #bdbdbd;
    --navy: #232c8e;
    --navy-deep: #1a2278;
    --navy-light: #3140b0;
    --sky: #3a9fe0;
    --ink: #2b2b2b;
    --paper: #ffffff;
  }
  * { margin: 0; padding: 0; box-sizing: border-box; }
  html, body { width: 1200px; height: 944px; overflow: hidden; }
  body {
    background: var(--bg);
    font-family: "Open Sans", sans-serif;
    position: relative;
  }
  .card {
    position: absolute;
    width: 620px;
    height: 354px;
    border-radius: 24px;
    overflow: hidden;
  }
  .card-back {
    left: 90px; top: 110px;
    background: radial-gradient(ellipse at 45% 40%, var(--navy-light) 0%, var(--navy) 55%, var(--navy-deep) 100%);
    color: var(--paper);
  }
  .card-back .brand-name {
    position: absolute;
    left: 0; right: 0; top: 118px;
    text-align: center;
    font-weight: 700;
    font-size: 44px;
    letter-spacing: 1px;
    color: var(--paper);
  }
  .card-back .website {
    position: absolute;
    left: 0; right: 0; top: 250px;
    text-align: center;
    font-size: 17px;
    letter-spacing: 1px;
  }
  .card-front {
    left: 490px; top: 480px;
    background: var(--paper);
    color: var(--ink);
  }
  .swoosh { position: absolute; inset: 0; width: 100%; height: 100%; }
  .card-front .brand-name {
    position: absolute;
    left: 46px; top: 52px;
    font-weight: 700;
    font-size: 34px;
    color: var(--navy);
    letter-spacing: 0.5px;
  }
  .contact-list {
    position: absolute;
    left: 44px; top: 214px;
    list-style: none;
    font-size: 17px;
    line-height: 22px;
  }
  .contact-list li { display: flex; align-items: center; gap: 10px; }
  .contact-list svg { width: 14px; height: 14px; flex: none; }
  .person {
    position: absolute;
    right: 48px; top: 216px;
    text-align: right;
  }
  .person .name { font-size: 20px; font-weight: 600; letter-spacing: 0.5px; }
  .person .role { font-size: 16px; color: var(--sky); letter-spacing: 0.5px; }
  .address {
    position: absolute;
    right: 48px; top: 286px;
    text-align: right;
    font-size: 16px;
    line-height: 21px;
  }
</style>
</head>
<body>

  <section class="card card-back" aria-label="Card back">
    <div class="brand-name">TARNWELL HOLDINGS</div>
    <div class="website">www.tarnwellholdings.com</div>
  </section>

  <section class="card card-front" aria-label="Card front">
    <svg class="swoosh" viewBox="0 0 620 354" preserveAspectRatio="none" aria-hidden="true">
      <path d="M400 0 C500 40 575 120 620 250 L620 0 Z" fill="var(--sky)"/>
      <path d="M470 0 C540 50 590 130 620 210 L620 0 Z" fill="var(--paper)"/>
      <path d="M490 0 C555 50 600 120 620 180 L620 0 Z" fill="var(--navy)"/>
      <path d="M440 0 C530 60 595 150 620 230 L620 222 C592 142 530 55 452 0 Z" fill="var(--sky)" opacity="0.6"/>
    </svg>

    <div class="brand-name">TARNWELL HOLDINGS</div>

    <ul class="contact-list">
      <li>
        <svg viewBox="0 0 14 14"><path d="M3 1 L5.5 1 L6.5 4 L5 5.5 C6 7.5 7 8.5 8.5 9 L10 7.5 L13 8.5 L13 11 C13 12 12 13 11 13 C5.5 12.5 1.5 8.5 1 3 C1 2 2 1 3 1 Z" fill="var(--sky)"/></svg>
        512-555-0140
      </li>
      <li>
        <svg viewBox="0 0 14 14"><rect x="3.5" y="0.5" width="7" height="13" rx="1.5" fill="var(--sky)"/><rect x="5" y="2.5" width="4" height="7" fill="var(--paper)"/></svg>
        512-555-0141
      </li>
      <li>
        <svg viewBox="0 0 14 14"><rect x="0.5" y="2.5" width="13" height="9" rx="1" fill="var(--sky)"/><path d="M1 3 L7 8 L13 3" stroke="var(--paper)" stroke-width="1.2" fill="none"/></svg>
        info@tarnwellholdings.com
      </li>
      <li>
        <svg viewBox="0 0 14 14"><circle cx="7" cy="7" r="6.5" fill="var(--sky)"/></svg>
        www.tarnwellholdings.com
      </li>
    </ul>

    <div class="person">
      <div class="name">Marcus Delaney</div>
      <div class="role">director</div>
    </div>

    <div class="address">
      1480 Alder Crest Rd<br>
      Harlow, TX 78110
    </div>
  </section>

</body>
</html>
```